Innovative coffee bean bag design for roasters

We need a design which can be printed on a coffee bean bag but which could also work on a sticker of similar size. We're after quirky, geeky, playful and innovative. Something that will stand out and communicate the character of our business. It should be eye catching and draw the customer in for a closer look.
Thematically, think organic and earthy.
It needs an element which can be changed for different coffee origins and roast profiles, so the main design will remain the same but with a feature which changes to help the customer know what they're looking at and will make them smile.
Approximate dimensions we need are 15cm by 12cm, with the 15cm being the vertical height of the bag image. (The image will be viewed in portrait). This is the main print area - however, if you have a great idea for a full bag image (approximately 23cm by 13cm), feel free to submit this too, we're interested in all ideas.
There is an image attached of a white partially see-through bag which we are considering using, so keep this in mind when designing.
We will need our logo including - see attached image.
Finally, we need space for the information about the coffee, such as origin, roast profile, flavour notes - see attached image for an example of the information (not necessarily a stylistic indicator). Please suggest fonts etc.

Target Market(s)

coffee roasters

Requirements
Must have
• Must say under the logo coffee roasters( Tiny Kettle Organic Coffee Roasters )
Nice to have
• Unique symbol, shapes, scientific.

```html
<!DOCTYPE html>
<html lang="en">
<head>
<meta charset="utf-8">
<title>Tiny Kettle Organic Coffee Roasters – Roasted Arabica Coffee Beans</title>
<link rel="stylesheet" href="https://fonts.googleapis.com/css2?family=Noto+Serif:ital,wght@0,400;0,700;1,400&display=swap">
<style>
  :root {
    --page: #ffffff;
    --bag: #f4f4f3;
    --bag-edge: #e6e6e4;
    --pattern-base: #f7f6f2;
    --pattern-tone: #ebe8df;
    --grid-line: #d6d1c3;
    --ribbon: #5a4a2c;
    --ribbon-dark: #3f321b;
    --ribbon-light: #8a7a5c;
    --cream: #d9d1bd;
    --leaf: #6cb33f;
    --ink: #4a3c22;
  }
  html, body {
    margin: 0;
    width: 1200px;
    height: 1200px;
    overflow: hidden;
    background: var(--page);
  }
  .canvas {
    width: 1200px;
    height: 1200px;
    display: block;
  }
  .band-text,
  .seal-name,
  .seal-sub,
  .label-roast,
  .label-variety,
  .label-product {
    font-family: "Noto Serif", Georgia, serif;
  }
  .band-text { font-size: 15px; font-style: italic; fill: var(--cream); letter-spacing: 0.3px; }
  .seal-name { font-size: 30px; font-weight: 700; fill: var(--leaf); }
  .seal-sub { font-size: 14px; font-style: italic; fill: var(--cream); }
  .label-roast { font-size: 22px; font-weight: 700; fill: var(--ink); }
  .label-variety { font-size: 28px; font-weight: 700; fill: var(--leaf); letter-spacing: 1.5px; }
  .label-product { font-size: 22px; font-weight: 700; fill: var(--ink); }
</style>
</head>
<body>
<svg class="canvas" viewBox="0 0 1200 1200" xmlns="http://www.w3.org/2000/svg">
  <defs>
    <linearGradient id="ribbon-sheen" x1="0" y1="0" x2="1" y2="0">
      <stop offset="0" stop-color="var(--ribbon)"/>
      <stop offset="0.25" stop-color="var(--ribbon-light)"/>
      <stop offset="0.7" stop-color="var(--ribbon-dark)"/>
      <stop offset="1" stop-color="var(--ribbon)"/>
    </linearGradient>
    <linearGradient id="pattern-fill" x1="0" y1="0" x2="1" y2="1">
      <stop offset="0" stop-color="var(--pattern-tone)"/>
      <stop offset="0.5" stop-color="var(--pattern-base)"/>
      <stop offset="1" stop-color="var(--pattern-tone)"/>
    </linearGradient>
    <pattern id="step-grid" width="80" height="80" patternUnits="userSpaceOnUse" patternTransform="rotate(-14)">
      <rect width="80" height="80" fill="none" stroke="var(--grid-line)" stroke-width="1"/>
    </pattern>
    <clipPath id="pattern-clip">
      <polygon points="324,220 881,220 881,769 324,869"/>
    </clipPath>
  </defs>

  <!-- bag panel -->
  <rect class="panel" x="324" y="220" width="557" height="870" fill="var(--bag)" stroke="var(--bag-edge)"/>

  <!-- brewing-step pattern area -->
  <g class="brew-pattern" clip-path="url(#pattern-clip)">
    <polygon role="img"
      aria-label="Repeating pattern of numbered line icons showing coffee brewing steps: pour-over, French press, moka pot, espresso machine and cezve"
      points="324,220 881,220 881,769 324,869" fill="url(#pattern-fill)"/>
    <rect class="step-grid" x="324" y="220" width="557" height="650" fill="url(#step-grid)"/>
  </g>

  <!-- diagonal band -->
  <polygon class="diagonal-band" points="324,652 881,512 881,552 324,692" fill="var(--ribbon)"/>
  <text class="band-text" transform="translate(364,681) rotate(-14)">Organic Coffee</text>
  <text class="band-text" transform="translate(748,582) rotate(-14)">Organic Coffee</text>

  <!-- vertical ribbon -->
  <polygon class="ribbon" points="517,220 692,220 692,847 604,825 517,847" fill="url(#ribbon-sheen)"/>
  <line x1="527" y1="220" x2="527" y2="840" stroke="var(--cream)" stroke-width="1.5"/>
  <line x1="684" y1="220" x2="684" y2="840" stroke="var(--cream)" stroke-width="1.5"/>

  <!-- seal -->
  <g class="seal">
    <circle cx="603" cy="609" r="135" fill="var(--ribbon-dark)"/>
    <circle cx="603" cy="609" r="120" fill="none" stroke="var(--cream)" stroke-width="2"/>
    <circle cx="603" cy="609" r="92" fill="var(--ribbon-dark)" stroke="var(--cream)" stroke-width="2"/>
    <text class="seal-name" x="603" y="606" text-anchor="middle">Tiny Kettle</text>
    <text class="seal-sub" x="603" y="640" text-anchor="middle">Organic Coffee Roasters</text>
  </g>

  <!-- product label -->
  <text class="label-roast" x="603" y="876" text-anchor="middle">Roasted</text>
  <text class="label-variety" x="603" y="910" text-anchor="middle">ARABICA</text>
  <text class="label-product" x="603" y="938" text-anchor="middle">Coffee Beans</text>
</svg>
</body>
</html>
```